Provide a Refreshed and Professional feel to our company brochure

We want to update and refresh our company brochure with up to date images of our current projects

The content of our current brochure is current, however, we would like to move away from the current design that incorporates a lot of circles.
The colour scheme of the brochure is spot on, but I would like to see some other layouts.

I would also like to incorporate some pages where we can showcase some completed projects.

At the back of the brochure, I would like to add a section labelled "Floor Plans" which will showcase some of our popular floor plans and facades that are available for construction. I would like to see one facade and one floor plan per A4 page.

I will have all of the files and photos in a dropbox folder, which can be accessed here -https://www.filevaultex.com/sh/3kd92mzqpa7xbe4/QRtuVmnbWeLpXcYdHsKfGaij?dl=0

Target Market(s)

1st, 2nd and forever home builders looking to build with a quality custom home builder

Industry/Entity Type

Residential Construction

Font styles to use
Sans Serif

Colors
0692cd
919191
fbfbfb

Requirements
Must have
• Lots of lifestyle images
• Professional but modern feel
Should not have
• Too much text and not enough images

```html
<!DOCTYPE html>
<html lang="en">
<head>
<meta charset="utf-8">
<title>Meridian 18 Homes – Brochure Spreads</title>
<link rel="stylesheet" href="https://fonts.googleapis.com/css2?family=Jost:wght@300;400;500;600;700&display=swap">
<style>
:root{
  --blue:#0692cd;
  --blue-deep:#0a7fb8;
  --grey:#919191;
  --grey-dark:#5d5d5d;
  --paper:#fbfbfb;
  --stage:#2f2f2f;
  --ink:#4a4a4a;
}
*{box-sizing:border-box;margin:0;padding:0}
html,body{width:1200px;height:3000px;overflow:hidden}
body{background:var(--stage);font-family:'Jost',sans-serif;color:var(--ink);position:relative}
.spread{position:absolute;left:100px;width:1000px;height:707px;display:flex;box-shadow:0 18px 40px rgba(0,0,0,.45)}
.spread--cover{top:34px}
.spread--welcome{top:775px}
.spread--why{top:1516px}
.spread--guarantees{top:2257px}
.page{position:relative;width:500px;height:707px;background:var(--paper);overflow:hidden}
.page--left::after{content:"";position:absolute;right:0;top:0;width:30px;height:100%;background:linear-gradient(to left,rgba(0,0,0,.12),rgba(0,0,0,0));pointer-events:none}
.page--right::after{content:"";position:absolute;left:0;top:0;width:30px;height:100%;background:linear-gradient(to right,rgba(0,0,0,.12),rgba(0,0,0,0));pointer-events:none}
.photo{position:absolute;display:block}
.photo--dining{background:linear-gradient(180deg,#f7f7f5 0%,#e9ebea 28%,#9fb4a2 46%,#d8d2c4 58%,#efe9dc 72%,#c9c4bb 100%)}
.photo--lounge{background:linear-gradient(180deg,#f3f5f6 0%,#dfe6e8 30%,#a9bfa6 45%,#cdbfa6 58%,#e6c874 66%,#b9ab96 80%,#8d7f6e 100%)}
.photo--kitchen-wide{background:linear-gradient(165deg,#f8f8f7 0%,#e8e8e6 35%,#c9c6c1 60%,#7a4a3c 72%,#d7d3cc 82%,#a8a39b 100%)}
.photo--kitchen-corner{background:linear-gradient(190deg,#f5f5f4 0%,#dededb 45%,#b8b3ab 75%,#8e877d 100%)}
.photo--family{background:linear-gradient(135deg,#7fae56 0%,#b6d08a 30%,#f0dcc0 50%,#e7b98c 65%,#8fb6d6 80%,#5e8b3c 100%)}
.photo--kitchen-bright{background:linear-gradient(175deg,#fafafa 0%,#ececea 40%,#d4d1cc 65%,#8a5f43 78%,#cfcac2 90%,#b3ada4 100%)}
.photo--bedroom{background:linear-gradient(170deg,#f4f2ef 0%,#e6dfd4 30%,#d9c9b4 55%,#b89d84 72%,#7b6656 88%,#5d4a3f 100%)}
.photo--plans{background:linear-gradient(150deg,#ffffff 0%,#eef2f5 40%,#c9d3db 70%,#9fb0be 100%)}
.blue-box{position:absolute;background:var(--blue);color:#fff}
.grey-tab{position:absolute;background:var(--grey-dark)}

/* cover back */
.back-heading{position:absolute;left:40px;top:44px;font-size:28px;font-weight:400;color:var(--grey)}
.back-heading strong{color:var(--blue);font-weight:600}
.back-rule{position:absolute;left:40px;top:88px;width:36px;height:3px;background:var(--blue)}
.back-sub{position:absolute;left:84px;top:82px;font-size:11px;color:var(--grey)}
.contact-btn{position:absolute;left:40px;top:500px;width:150px;height:36px;background:var(--blue);color:#fff;font-size:13px;font-weight:500;display:flex;align-items:center;justify-content:center}
.contact-list{position:absolute;left:40px;top:556px;list-style:none;font-size:12.5px;color:var(--grey-dark)}
.contact-list li{display:flex;align-items:center;gap:10px;height:28px}
.contact-list svg{width:14px;height:14px;flex:none}
.contact-list .web{color:var(--blue);font-weight:600;font-size:14px}
.badge{position:absolute;background:#c9c9c9}

/* front cover */
.brand{position:absolute;right:40px;top:36px;display:flex;align-items:center;gap:8px;font-size:20px;font-weight:600;color:var(--blue);letter-spacing:.5px}
.brand .dot{width:12px;height:12px;border-radius:50%;background:var(--blue)}
.cover-band{position:absolute;left:150px;top:470px;width:350px;height:88px;background:var(--blue);color:#fff;text-align:right;padding:16px 36px 0 0}
.cover-band .region{font-size:19px;font-weight:600}
.cover-band .tag{font-size:19px;font-weight:300}
.cover-web{position:absolute;left:40px;top:640px;display:flex;align-items:center;gap:8px;font-size:12.5px;color:var(--grey-dark)}
.cover-web svg{width:14px;height:14px}

/* welcome */
.title-box{padding:26px 30px}
.title-box h2{font-size:27px;font-weight:600;line-height:1.15}
.title-box h2 span{display:block;font-weight:300}
.title-box p{margin-top:12px;font-size:11px;line-height:1.55;font-weight:300}
.quote-box{padding:26px 30px}
.quote-mark{font-size:50px;line-height:1;font-weight:700;display:block;height:34px}
.quote-mark--end{text-align:right;margin-top:6px}
.quote-box p{font-size:13px;line-height:1.65;font-weight:300;margin-top:10px}
.quote-box cite{display:block;text-align:right;font-style:normal;font-size:12px;margin-top:14px;font-weight:500}

/* why build */
.feature-list{position:absolute;left:40px;top:36px;width:425px;list-style:none}
.feature-list li{margin-bottom:12px}
.feature-list h3{font-size:12px;font-weight:600;color:var(--blue);text-transform:uppercase;letter-spacing:.3px}
.feature-list p{font-size:11px;line-height:1.5;color:var(--grey-dark);margin-top:3px}
.testimonial-band{position:absolute;top:560px;width:560px;height:120px;background:var(--blue);color:#fff;padding:12px 26px}
.testimonial-band .quote-mark{font-size:42px;height:26px}
.testimonial-band p{font-size:12px;line-height:1.55;font-weight:300;padding-left:40px;width:470px}
.testimonial-band cite{position:absolute;right:80px;bottom:30px;font-style:normal;font-size:12px;font-weight:500}
.testimonial-band .quote-mark--end{position:absolute;right:28px;bottom:16px}

/* guarantees */
.guarantee-band{position:absolute;left:0;top:36px;width:500px;height:160px;background:var(--blue);color:#fff;padding:24px 40px}
.guarantee-band h2{font-size:28px;font-weight:600}
.guarantee-band h2 span{font-weight:300}
.guarantee-band p{margin-top:12px;font-size:12px;line-height:1.55;font-weight:300}
.guarantee-band strong{font-weight:700}
.promise-box{padding:18px 24px;font-size:12.5px;line-height:1.55;font-weight:300}
.seal{position:absolute;width:80px;height:80px;border-radius:50%;background:var(--blue-deep);border:4px solid #d7e6ee}
.guarantee-list{position:absolute;left:40px;top:400px;width:370px}
.guarantee-list h3{font-size:12px;font-weight:600;color:var(--blue);text-transform:uppercase;margin-top:16px}
.guarantee-list p{font-size:11px;line-height:1.55;color:var(--grey-dark);margin-top:4px}
</style>
</head>
<body>

<section class="spread spread--cover">
  <div class="page page--left back-cover">
    <h2 class="back-heading">Feeling <strong>Excited?</strong></h2>
    <span class="back-rule"></span>
    <p class="back-sub">Keep scrolling to view all our beautiful new home designs</p>
    <div class="photo photo--dining" style="left:0;top:120px;width:500px;height:398px" role="img" aria-label="Photo of a bright open-plan kitchen and dining area with pendant lights and garden views"></div>
    <div class="contact-btn">Contact Info</div>
    <ul class="contact-list">
      <li><svg viewBox="0 0 16 16"><path d="M3 1h3l1.5 4-2 1.2a9 9 0 0 0 4.3 4.3L11 8.5l4 1.5v3a2 2 0 0 1-2 2A12 12 0 0 1 1 3a2 2 0 0 1 2-2z" fill="var(--blue)"/></svg>07 4000 1234</li>
      <li><svg viewBox="0 0 16 16"><rect x="1" y="3" width="14" height="10" rx="1" fill="none" stroke="var(--blue)" stroke-width="1.6"/><path d="M1.5 4l6.5 5 6.5-5" fill="none" stroke="var(--blue)" stroke-width="1.6"/></svg>hello@meridian18homes.com.au</li>
      <li><svg viewBox="0 0 16 16"><circle cx="8" cy="8" r="6.5" fill="none" stroke="var(--blue)" stroke-width="1.6"/><path d="M1.5 8h13M8 1.5c3 3 3 10 0 13M8 1.5c-3 3-3 10 0 13" fill="none" stroke="var(--blue)" stroke-width="1.2"/></svg><span class="web">www.meridian18homes.com.au</span></li>
    </ul>
    <span class="badge" style="left:300px;top:600px;width:40px;height:28px"></span>
    <span class="badge" style="left:352px;top:598px;width:42px;height:32px"></span>
    <span class="badge" style="left:406px;top:600px;width:28px;height:28px;border-radius:50%"></span>
  </div>
  <div class="page page--right front-cover">
    <div class="brand"><span class="dot"></span>MERIDIAN 18 HOMES</div>
    <div class="photo photo--lounge" style="left:0;top:90px;width:500px;height:430px" role="img" aria-label="Photo of a modern living room with a sectional sofa, cushions and large glass doors"></div>
    <div class="cover-band">
      <div class="region">Bowen &amp; Whitsundays</div>
      <div class="tag">Custom Home Building Specialists</div>
    </div>
    <div class="cover-web"><svg viewBox="0 0 16 16"><circle cx="8" cy="8" r="6.5" fill="none" stroke="var(--blue)" stroke-width="1.6"/><path d="M1.5 8h13M8 1.5c3 3 3 10 0 13M8 1.5c-3 3-3 10 0 13" fill="none" stroke="var(--blue)" stroke-width="1.2"/></svg>www.meridian18homes.com.au</div>
  </div>
</section>

<section class="spread spread--welcome">
  <div class="page page--left">
    <div class="photo photo--kitchen-wide" style="left:0;top:0;width:500px;height:540px" role="img" aria-label="Photo of a white kitchen with an island bench and timber French doors"></div>
    <div class="blue-box title-box" style="left:30px;top:400px;width:320px;height:196px">
      <h2>Welcome to <span>Meridian 18 Homes</span></h2>
      <p>We're more than just a home builder. We're passionate about creating quality custom homes that reflect the way you live, designed and built by a local team who care.</p>
    </div>
  </div>
  <div class="page page--right">
    <div class="photo photo--kitchen-corner" style="left:0;top:0;width:500px;height:400px" role="img" aria-label="Photo of a kitchen corner with wall oven and pendant light"></div>
    <div class="blue-box quote-box" style="left:230px;top:60px;width:270px;height:310px">
      <span class="quote-mark">&ldquo;</span>
      <p>From our first meeting to handing over the keys, the team made every step simple. We couldn't be happier with our new home and the care shown throughout.</p>
      <cite>Daniel Reyes</cite>
      <span class="quote-mark quote-mark--end">&rdquo;</span>
    </div>
    <div class="photo photo--family" style="left:50px;top:400px;width:380px;height:250px" role="img" aria-label="Photo of a family sharing an outdoor meal in a sunny garden"></div>
  </div>
</section>

<section class="spread spread--why">
  <div class="page page--left">
    <div class="photo photo--kitchen-bright" style="left:0;top:0;width:500px;height:560px" role="img" aria-label="Photo of a bright kitchen with a timber stool and pendant lights"></div>
    <div class="blue-box title-box" style="left:90px;top:410px;width:330px;height:112px">
      <h2>Why Build With <span>Meridian 18 Homes?</span></h2>
    </div>
  </div>
  <div class="page page--right">
    <ul class="feature-list">
      <li><h3>1. Project Management</h3><p>Your build is guided by one dedicated supervisor from the first site visit right through to the final handover.</p></li>
      <li><h3>2. Exceptional Customer Care and Superior Communication</h3><p>We keep you informed at every stage with regular updates, site meetings and clear answers to your questions.</p></li>
      <li><h3>3. Quality Finishes</h3><p>We use trusted trades and premium materials so every home is finished to a standard you can be proud of.</p></li>
      <li><h3>4. Personal Approach</h3><p>Every family is different, so we take the time to understand how you live and design around it.</p></li>
      <li><h3>5. Local Experience</h3><p>Our team knows the region, its climate and its councils, making the approval process smooth and simple.</p></li>
      <li><h3>6. Flexible Designs</h3><p>Choose from our popular plans or create something completely new with our in-house design team.</p></li>
      <li><h3>7. Quality Guarantee</h3><p>Every home is backed by our structural warranty and our commitment to stand behind our work.</p></li>
    </ul>
    <div class="grey-tab" style="left:430px;top:560px;width:70px;height:147px"></div>
  </div>
  <div class="testimonial-band" style="left:250px">
    <span class="quote-mark">&ldquo;</span>
    <p>We set out to build our dream home and the team delivered beyond our expectations. Every detail was handled with care and we would recommend them to anyone.</p>
    <cite>Sarah &amp; Tom</cite>
    <span class="quote-mark quote-mark--end">&rdquo;</span>
  </div>
</section>

<section class="spread spread--guarantees">
  <div class="page page--left">
    <div class="guarantee-band">
      <h2>Our <span>Guarantees</span></h2>
      <p>We want you to be confident in your build, which is why every home we build is backed by our promise to deliver your new home <strong>ON TIME</strong> and <strong>ON BUDGET</strong>.</p>
    </div>
    <div class="photo photo--bedroom" style="left:0;top:196px;width:500px;height:450px" role="img" aria-label="Photo of a styled bedroom with a linen-covered bed, shutters and wall art"></div>
  </div>
  <div class="page page--right">
    <div class="photo photo--plans" style="left:30px;top:30px;width:470px;height:250px" role="img" aria-label="Photo of rolled architectural house plans on a desk"></div>
    <div class="seal" style="left:370px;top:290px"></div>
    <div class="guarantee-list">
      <h3>Fixed Price Guarantee</h3>
      <p>Once your contract is signed, the price is locked in. No hidden costs and no surprises, so you can plan your future with certainty.</p>
      <h3>On Time Guarantee</h3>
      <p>We agree on a completion date before we start, and we stand by it. If we run late, we compensate you for every extra day.</p>
    </div>
    <div class="grey-tab" style="left:440px;top:570px;width:60px;height:137px"></div>
  </div>
  <div class="blue-box promise-box" style="left:420px;top:265px;width:340px;height:100px">
    Our Fixed Price and On Time Guarantees give you peace of mind from the day you sign to the day you move in.
  </div>
</section>

</body>
</html>
```